Harbor Lantern Business Card
remarkable business card
Project: Harbor Lantern Business Card
Harbor Lantern Business Card - Events
Creative Brief
Use specific fonts
Use the fonts in my logo and/or the fonts that look best
Bright & Fun-filled
Tom Vesk
Culture Director
not to be listed on the card
Vesk@HarborLantern.example
www.HarborLantern.example
I want the Name to be prominent . I don't want the address to be listed This should be a very remarkable card. It needs to get instant attention that people will remember, and talk about. People should say wow! you need to see this card. That is a great looking card!

```html
<!DOCTYPE html>
<html lang="en">
<head>
<meta charset="utf-8">
<title>Harbor Lantern Business Card</title>
<link href="https://fonts.googleapis.com/css2?family=Tinos:wght@400;700&display=swap" rel="stylesheet">
<style>
  :root {
    --backdrop: #ece7df;
    --card-white: #ffffff;
    --card-shade: #e9eaea;
    --green-dark: #1f7a2c;
    --green-mid: #3f9a35;
    --green-light: #8cc63f;
    --text-light: #ffffff;
    --brand-green: #3c8f2f;
  }
  html, body {
    margin: 0;
    padding: 0;
    width: 1200px;
    height: 763px;
    overflow: hidden;
    background: var(--backdrop);
  }
  .canvas {
    position: relative;
    width: 1200px;
    height: 763px;
    font-family: "Tinos", "Times New Roman", serif;
  }
  .card {
    position: absolute;
    border-radius: 12px;
    overflow: hidden;
    box-shadow: 0 6px 14px rgba(0,0,0,0.25);
  }
  .card svg { position: absolute; inset: 0; }

  .brand {
    position: absolute;
    display: flex;
    align-items: center;
    gap: 14px;
    color: var(--brand-green);
    font-weight: 400;
    white-space: nowrap;
  }
  .brand-dot {
    border-radius: 50%;
    background: var(--brand-green);
    flex: none;
  }

  /* Front card */
  .card-front {
    left: 110px; top: 115px; width: 500px; height: 288px;
    z-index: 2;
    background: linear-gradient(180deg, var(--card-white), var(--card-shade));
  }
  .card-front .brand { left: 28px; top: 30px; font-size: 40px; }
  .card-front .brand-dot { width: 64px; height: 64px; }
  .holder {
    position: absolute;
    left: 62px;
    width: 210px;
    top: 200px;
    text-align: center;
    color: var(--text-light);
  }
  .holder-name { font-size: 21px; font-weight: 700; }
  .holder-role { font-size: 13.5px; margin-top: 2px; }
  .divider {
    position: absolute;
    left: 226px;
    top: 188px;
    width: 1px;
    height: 82px;
    background: rgba(255,255,255,0.6);
  }
  .contact {
    position: absolute;
    left: 238px;
    top: 190px;
    color: var(--text-light);
    font-size: 13.5px;
    line-height: 19px;
  }

  /* Green back card */
  .card-back {
    left: 665px; top: 34px; width: 362px; height: 278px;
    z-index: 1;
    background: linear-gradient(100deg, var(--green-light), var(--green-mid) 55%, var(--green-dark));
  }
  .card-back .brand { right: 18px; bottom: 46px; font-size: 26px; color: var(--text-light); }

  /* White back card */
  .card-white {
    left: 422px; top: 355px; width: 495px; height: 288px;
    z-index: 1;
    background: linear-gradient(180deg, var(--card-white), var(--card-shade));
  }
  .card-white .brand { right: 22px; bottom: 48px; font-size: 30px; }
</style>
</head>
<body>
<main class="canvas">

  <section class="card card-back" aria-label="Business card back, green">
    <svg width="362" height="278" viewBox="0 0 362 278">
      <defs>
        <radialGradient id="back-deco" cx="0.5" cy="0.5" r="0.5">
          <stop offset="0" stop-color="#d6f0a8" stop-opacity="0.45"/>
          <stop offset="1" stop-color="#d6f0a8" stop-opacity="0"/>
        </radialGradient>
      </defs>
      <rect x="0" y="0" width="250" height="250" fill="url(#back-deco)" role="img" aria-label="Faint large brand symbol decoration"/>
    </svg>
    <div class="brand">Harbor Lantern</div>
  </section>

  <section class="card card-white" aria-label="Business card back, white">
    <svg width="495" height="288" viewBox="0 0 495 288">
      <defs>
        <linearGradient id="white-deco" x1="0" y1="0" x2="1" y2="1">
          <stop offset="0" stop-color="#f4b48a" stop-opacity="0.55"/>
          <stop offset="0.5" stop-color="#b9dc8c" stop-opacity="0.5"/>
          <stop offset="1" stop-color="#8fb2e4" stop-opacity="0.55"/>
        </linearGradient>
      </defs>
      <rect x="0" y="0" width="250" height="288" fill="url(#white-deco)" role="img" aria-label="Soft multicolour brand symbol decoration"/>
    </svg>
    <div class="brand">Harbor Lantern</div>
  </section>

  <section class="card card-front" aria-label="Business card front">
    <svg width="500" height="288" viewBox="0 0 500 288" aria-hidden="true">
      <defs>
        <linearGradient id="band-green" x1="0" y1="0" x2="1" y2="1">
          <stop offset="0" stop-color="#4fa83a"/>
          <stop offset="0.5" stop-color="#2b8a30"/>
          <stop offset="1" stop-color="#15661f"/>
        </linearGradient>
      </defs>
      <path d="M0 150 C120 175 300 150 500 112 L500 288 L0 288 Z" fill="#8fc96a" opacity="0.6"/>
      <path d="M0 160 C140 182 310 158 500 122 L500 288 L0 288 Z" fill="url(#band-green)"/>
    </svg>
    <div class="brand"><span class="brand-dot"></span>Harbor Lantern</div>
    <div class="holder">
      <div class="holder-name">Tom Vesk</div>
      <div class="holder-role">Culture Director</div>
    </div>
    <div class="divider"></div>
    <div class="contact">
      <div>Cell: 555-210-4837</div>
      <div>Fax: 555-210-4838</div>
      <div>Vesk@HarborLantern.example</div>
      <div>www.HarborLantern.example</div>
    </div>
  </section>

</main>
</body>
</html>
```